PROPERTY MANAGEMENT AND REAL ESTATE

Target Market(s)

real estate owners and investors

Industry/Entity Type

Real Estate

Contact Information for Business Card

BRIGHT HARBOR PROPERTY MANAGEMENT GROUP, LLC
287 West Marlow Parkway
Suite 240
Marlow Springs, FL 33150

```html
<!DOCTYPE html>
<html lang="en">
<head>
<meta charset="utf-8">
<title>Bright Harbor Property Management Group – Business Cards</title>
<link href="https://fonts.googleapis.com/css2?family=Roboto:wght@400;700;900&family=Nunito+Sans:wght@300&display=swap" rel="stylesheet">
<style>
  :root {
    --brand-red: #8b2a2a;
    --card-white: #f7f7f7;
    --ink: #3a3a3a;
    --backdrop: #e9e9e9;
  }
  * { margin: 0; padding: 0; box-sizing: border-box; }
  html, body { width: 1200px; height: 1001px; overflow: hidden; }
  body {
    background: var(--backdrop);
    font-family: "Roboto", Arial, sans-serif;
    position: relative;
  }
  .card {
    position: absolute;
    width: 504px;
    height: 288px;
    background: var(--brand-red);
    overflow: hidden;
    box-shadow: 0 10px 24px rgba(0,0,0,0.12);
  }
  .card-face {
    position: absolute;
    inset: 0;
    background: var(--card-white);
  }
  /* Front card: contact details */
  .card--front { left: 72px; top: 356px; }
  .card--front .card-face { border-top-right-radius: 70px; }
  .company-name {
    position: absolute;
    left: 34px; top: 34px;
    width: 400px;
    color: var(--brand-red);
    font-weight: 900;
    font-size: 22px;
    line-height: 1.05;
    letter-spacing: 0.2px;
  }
  .contact-list {
    position: absolute;
    left: 34px; top: 112px;
    list-style: none;
    color: var(--ink);
    font-size: 14px;
    line-height: 19px;
  }
  .contact-list li { display: flex; align-items: flex-start; gap: 12px; }
  .contact-icon { width: 14px; height: 19px; flex: none; }
  .contact-icon svg { width: 14px; height: 14px; margin-top: 2px; fill: var(--brand-red); }
  .lockup {
    position: absolute;
    display: flex;
    align-items: center;
    gap: 14px;
  }
  .lockup-dot {
    flex: none;
    border-radius: 50%;
    background: var(--brand-red);
  }
  .lockup-name {
    font-family: "Nunito Sans", Arial, sans-serif;
    font-weight: 300;
    color: var(--ink);
    line-height: 1.15;
    letter-spacing: 0.3px;
  }
  .card--front .lockup { right: 28px; bottom: 26px; }
  .card--front .lockup-dot { width: 40px; height: 40px; }
  .card--front .lockup-name { font-size: 12px; }

  /* Back card: brand lockup */
  .card--back { left: 624px; top: 356px; }
  .card--back .card-face { border-top-left-radius: 70px; border-bottom-right-radius: 70px; }
  .card--back .lockup { left: 64px; top: 110px; }
  .card--back .lockup-dot { width: 58px; height: 58px; }
  .card--back .lockup-name { font-size: 17px; }
</style>
</head>
<body>
  <section class="card card--front" aria-label="Business card front">
    <div class="card-face">
      <h1 class="company-name">BRIGHT HARBOR PROPERTY MANAGEMENT GROUP, LLC</h1>
      <ul class="contact-list">
        <li>
          <span class="contact-icon"><svg viewBox="0 0 24 24" aria-hidden="true"><path d="M12 2a7 7 0 0 0-7 7c0 5 7 13 7 13s7-8 7-13a7 7 0 0 0-7-7zm0 9.5A2.5 2.5 0 1 1 12 6.5a2.5 2.5 0 0 1 0 5z"/></svg></span>
          <span>287 West Marlow Parkway Suite 240<br>Marlow Springs, FL 33150</span>
        </li>
        <li>
          <span class="contact-icon"><svg viewBox="0 0 24 24" aria-hidden="true"><path d="M6.6 10.8a15.1 15.1 0 0 0 6.6 6.6l2.2-2.2a1 1 0 0 1 1-.25 11.4 11.4 0 0 0 3.6.57 1 1 0 0 1 1 1V20a1 1 0 0 1-1 1A17 17 0 0 1 3 4a1 1 0 0 1 1-1h3.5a1 1 0 0 1 1 1c0 1.25.2 2.45.57 3.6a1 1 0 0 1-.25 1z"/></svg></span>
          <span>305-555-0148</span>
        </li>
        <li>
          <span class="contact-icon"><svg viewBox="0 0 24 24" aria-hidden="true"><path d="M6 2h9l3 3v5h1a3 3 0 0 1 3 3v7a2 2 0 0 1-2 2H4a2 2 0 0 1-2-2v-7a3 3 0 0 1 3-3h1zm2 2v6h8V6h-3V4zm-2 10v2h2v-2zm4 0v2h2v-2zm4 0v2h2v-2z"/></svg></span>
          <span>786-555-0193</span>
        </li>
      </ul>
      <div class="lockup">
        <span class="lockup-name">BRIGHT HARBOR PROPERTY<br>MANAGEMENT GROUP LLC.</span>
        <span class="lockup-dot" aria-hidden="true"></span>
      </div>
    </div>
  </section>

  <section class="card card--back" aria-label="Business card back">
    <div class="card-face">
      <div class="lockup">
        <span class="lockup-dot" aria-hidden="true"></span>
        <span class="lockup-name">BRIGHT HARBOR PROPERTY<br>MANAGEMENT GROUP LLC.</span>
      </div>
    </div>
  </section>
</body>
</html>
```